Wordpress Design for a Private Label BBQ Brand

For our new brand, we'd need a new Wordpress website. We'd prefer to run the website on Wordpress

We'd like to include the following
- space for description of the brand
- space for product portfolio (not a shop!)
- space for socials
- space for support
- space for contact

```html
<!DOCTYPE html>
<html lang="en">
<head>
<meta charset="utf-8">
<title>Brasato – Barbeque Grill Tools</title>
<link rel="stylesheet" href="https://fonts.googleapis.com/css2?family=Playfair+Display:wght@700;800&family=Poppins:wght@400;500;600;700&display=swap">
<style>
:root{
  --orange:#ec4a1c;
  --orange-light:#f47a2a;
  --red:#c9241a;
  --black:#0d0d0d;
  --dark:#1a1a1a;
  --grey:#6b6b6b;
  --light:#f3f3f3;
  --white:#ffffff;
  --serif:'Playfair Display', Georgia, serif;
  --sans:'Poppins', Arial, sans-serif;
}
*{box-sizing:border-box;margin:0;padding:0}
html,body{width:1200px;height:3692px;overflow:hidden;background:var(--white)}
body{font-family:var(--sans);color:var(--dark)}
.page{position:relative;width:1200px;height:3692px;overflow:hidden}

/* header */
.site-header{position:absolute;top:0;left:0;width:1200px;height:110px;background:var(--black);display:flex;align-items:center;justify-content:space-between;padding:0 70px;z-index:3}
.brand{display:flex;align-items:center;gap:14px;color:var(--white);font-family:var(--sans);font-weight:700;font-size:34px;letter-spacing:1px}
.brand-dot{width:34px;height:34px;border-radius:50%;background:var(--orange)}
.main-nav{display:flex;gap:30px;font-size:15px;color:var(--white)}
.main-nav span.sep{color:var(--orange)}

/* hero */
.hero{position:absolute;top:110px;left:0;width:1200px;height:790px}
.hero-photo{position:absolute;inset:0;background:radial-gradient(ellipse at 45% 70%,#9a3a1c 0%,#5a2010 30%,#1e0d07 65%,#0b0605 100%)}
.hero-text{position:absolute;top:90px;width:100%;text-align:center;color:var(--white)}
.hero-title{font-family:var(--serif);font-weight:800;font-size:76px;line-height:1.1}
.hero-title em{font-style:normal;color:var(--orange)}
.hero-sub{font-size:30px;font-weight:500;margin-top:10px}
.btn{display:inline-flex;align-items:center;gap:10px;background:var(--red);color:var(--white);font-weight:700;font-size:17px;padding:12px 34px;border-radius:30px;margin-top:26px}
.slider-arrow{position:absolute;top:320px;width:50px;height:50px;border-radius:50%;border:2px solid var(--white);display:flex;align-items:center;justify-content:center}
.slider-arrow.prev{left:40px}
.slider-arrow.next{right:40px}
.hero-swoosh{position:absolute;left:0;bottom:0;width:1200px;height:170px}

/* about */
.about{position:absolute;top:900px;left:0;width:1200px;height:640px;background:var(--white)}
.about-photo{position:absolute;left:70px;top:-20px;width:500px;height:500px;border-radius:50%;background:radial-gradient(circle at 50% 60%,#c3341a 0%,#5a1a10 45%,#1b0c08 80%);border:8px solid var(--light)}
.about-body{position:absolute;left:630px;top:30px;width:500px}
.eyebrow{font-size:17px;font-weight:500;display:flex;align-items:center;gap:14px}
.eyebrow::after{content:"";width:110px;height:2px;background:var(--orange)}
.about-title{font-family:var(--serif);font-weight:800;color:var(--orange);font-size:44px;line-height:1.12;margin:12px 0 18px}
.about-body p{font-size:14px;line-height:1.75;color:var(--grey);margin-bottom:14px}

/* products */
.products{position:absolute;top:1540px;left:0;width:1200px;height:1130px;background:linear-gradient(180deg,#1c1c1c,#0e0e0e 60%,#161616)}
.section-mark{width:44px;height:44px;border-radius:50%;background:var(--orange);margin:60px auto 14px}
.section-title{font-family:var(--serif);font-weight:800;color:var(--white);font-size:46px;text-align:center;display:flex;align-items:center;justify-content:center;gap:20px}
.section-title::before,.section-title::after{content:"";width:60px;height:2px;background:var(--orange)}
.product-grid{position:absolute;top:220px;left:90px;width:1020px;display:grid;grid-template-columns:repeat(4,1fr);grid-auto-rows:400px;gap:40px 30px}
.product-card{position:relative;background:var(--white);border-radius:12px;overflow:hidden;padding:20px}
.product-card.wide{grid-column:span 2}
.product-card::after{content:"";position:absolute;left:0;bottom:0;width:90px;height:12px;background:var(--orange)}
.product-card::before{content:"";position:absolute;right:0;top:0;width:12px;height:80px;background:var(--orange)}
.product-img{height:270px;border-radius:8px;background:linear-gradient(160deg,#e6e6e6,#b9b9b9)}
.product-card.wide .product-img{background:linear-gradient(90deg,#cfcfcf,#f0f0f0 50%,#f9d9c9)}
.product-name{font-family:var(--serif);font-weight:700;color:var(--orange);font-size:21px;margin-top:16px}
.product-tag{font-size:13px;color:var(--dark);margin-top:4px}

/* contact */
.contact{position:absolute;top:2670px;left:0;width:1200px;height:600px;background:linear-gradient(120deg,#b81c16,var(--orange) 55%,var(--orange-light))}
.contact-inner{position:absolute;left:70px;top:50px;width:560px;color:var(--white)}
.contact .eyebrow::after{background:var(--white)}
.contact-title{font-family:var(--serif);font-weight:800;font-size:50px;margin:6px 0 26px}
.form-row{display:flex;gap:16px;margin-bottom:16px}
.field{flex:1;height:46px;background:var(--white);border-radius:4px;font-size:12px;color:#999;padding:14px}
.field.area{height:130px}
.send{width:100%;height:46px;background:var(--black);color:var(--white);font-weight:600;font-size:14px;display:flex;align-items:center;justify-content:center;border-radius:4px}
.contact-photo{position:absolute;right:80px;top:60px;width:480px;height:480px;border-radius:50%;background:radial-gradient(circle at 50% 50%,#d86a2c 0%,#7a2a14 40%,#222 70%,#111 100%);border:10px solid rgba(255,255,255,.25)}

/* footer */
.site-footer{position:absolute;top:3270px;left:0;width:1200px;height:422px;background:var(--white)}
.footer-col{position:absolute;top:60px}
.footer-col h4{color:var(--orange);font-size:17px;font-weight:700;margin-bottom:16px}
.footer-col ul{list-style:none;font-size:15px;line-height:2}
.contact-line{display:flex;align-items:flex-start;gap:12px;font-size:15px;margin-bottom:16px;line-height:1.5}
.icon{flex:none;width:30px;height:30px;border-radius:50%;background:var(--orange);display:flex;align-items:center;justify-content:center}
.footer-map{position:absolute;left:640px;top:70px;width:250px;height:170px;border-radius:8px;background:linear-gradient(135deg,#e4e8e2,#cfd8d4);border:1px solid #ddd}
.footer-brand{position:absolute;left:950px;top:90px;width:200px;text-align:center}
.footer-brand .brand{color:var(--dark);justify-content:center;font-size:30px}
.follow{display:flex;align-items:center;justify-content:center;gap:8px;margin-top:50px;font-size:15px}
.social{width:26px;height:26px;border-radius:50%;background:var(--orange)}
.copyright{position:absolute;left:0;bottom:0;width:1200px;height:50px;background:var(--black);color:var(--white);font-size:13px;display:flex;align-items:center;justify-content:center}
</style>
</head>
<body>
<div class="page">

  <header class="site-header">
    <div class="brand"><span class="brand-dot"></span>BRASATO</div>
    <nav class="main-nav">
      <span>Home</span><span class="sep">|</span>
      <span>About</span><span class="sep">|</span>
      <span>Products</span><span class="sep">|</span>
      <span>Support Us</span><span class="sep">|</span>
      <span>Contact</span>
    </nav>
  </header>

  <section class="hero">
    <div class="hero-photo" role="img" aria-label="Steaks searing on a flaming barbecue grill with tongs"></div>
    <div class="hero-text">
      <h1 class="hero-title">Welcome To <em>Brasato</em></h1>
      <p class="hero-sub">The Best Barbeque Grill Tools</p>
      <span class="btn">READ MORE
        <svg width="14" height="14" viewBox="0 0 14 14"><path d="M2 7h9M7 3l4 4-4 4" stroke="#fff" stroke-width="2" fill="none"/></svg>
      </span>
    </div>
    <div class="slider-arrow prev"><svg width="16" height="16" viewBox="0 0 16 16"><path d="M10 3 5 8l5 5" stroke="#fff" stroke-width="2" fill="none"/></svg></div>
    <div class="slider-arrow next"><svg width="16" height="16" viewBox="0 0 16 16"><path d="m6 3 5 5-5 5" stroke="#fff" stroke-width="2" fill="none"/></svg></div>
    <svg class="hero-swoosh" viewBox="0 0 1200 170" preserveAspectRatio="none">
      <path d="M0 110 C300 40 700 40 1200 120 L1200 170 L0 170Z" fill="#f47a2a"/>
      <path d="M0 135 C320 70 720 70 1200 140 L1200 170 L0 170Z" fill="#ec4a1c"/>
      <path d="M0 155 C320 100 720 100 1200 160 L1200 170 L0 170Z" fill="#ffffff"/>
    </svg>
  </section>

  <section class="about">
    <div class="about-photo" role="img" aria-label="Black ceramic kamado grill over glowing embers"></div>
    <div class="about-body">
      <p class="eyebrow">About Brasato</p>
      <h2 class="about-title">THE BEST BARBEQUE<br>GRILL TOOLS</h2>
      <p>Lorem Ipsum is simply dummy text of the printing and typesetting industry. Lorem Ipsum has been the industry's standard dummy text ever since the 1500s, when an unknown printer took a galley of type and scrambled it to make a type specimen book. It has survived not only five centuries, but also the leap into electronic typesetting, remaining essentially unchanged.</p>
      <p>Lorem Ipsum is simply dummy text of the printing and typesetting industry. Lorem Ipsum has been the industry's standard dummy text ever since the 1500s, when an unknown printer took a galley of type and scrambled it to make a type specimen book. It has survived not only five centuries, but also the leap into electronic typesetting, remaining essentially unchanged.</p>
      <span class="btn">READ MORE
        <svg width="14" height="14" viewBox="0 0 14 14"><path d="M2 7h9M7 3l4 4-4 4" stroke="#fff" stroke-width="2" fill="none"/></svg>
      </span>
    </div>
  </section>

  <section class="products">
    <div class="section-mark"></div>
    <h2 class="section-title">OUR PRODUCTS</h2>
    <div class="product-grid">
      <article class="product-card wide">
        <div class="product-img" role="img" aria-label="Stainless steel grill spatula"></div>
        <h3 class="product-name">Brasato-3pc-2</h3>
        <p class="product-tag">Barbeque Grill Tools</p>
      </article>
      <article class="product-card">
        <div class="product-img" role="img" aria-label="Compact black kamado grill"></div>
        <h3 class="product-name">Brasato-1Inch-1</h3>
        <p class="product-tag">Barbeque Grill Tools</p>
      </article>
      <article class="product-card">
        <div class="product-img" role="img" aria-label="Open grill tool set case"></div>
        <h3 class="product-name">Brasato-15pcs-3</h3>
        <p class="product-tag">Barbeque Grill Tools</p>
      </article>
      <article class="product-card">
        <div class="product-img" role="img" aria-label="Closed aluminium tool case"></div>
        <h3 class="product-name">Brasato-15pcs-3</h3>
        <p class="product-tag">Barbeque Grill Tools</p>
      </article>
      <article class="product-card">
        <div class="product-img" role="img" aria-label="Grill scraper tool"></div>
        <h3 class="product-name">Brasato-15pcs-5</h3>
        <p class="product-tag">Barbeque Grill Tools</p>
      </article>
      <article class="product-card">
        <div class="product-img" role="img" aria-label="Basting brush"></div>
        <h3 class="product-name">Brasato-15pcs-6</h3>
        <p class="product-tag">Barbeque Grill Tools</p>
      </article>
      <article class="product-card">
        <div class="product-img" role="img" aria-label="Salt and pepper grinders"></div>
        <h3 class="product-name">Brasato-15pcs-7</h3>
        <p class="product-tag">Barbeque Grill Tools</p>
      </article>
    </div>
  </section>

  <section class="contact">
    <div class="contact-inner">
      <p class="eyebrow">Brasato</p>
      <h2 class="contact-title">CONTACT FORM</h2>
      <div class="form-row"><div class="field">FIRST NAME</div><div class="field">LAST NAME</div></div>
      <div class="form-row"><div class="field">E-MAIL</div><div class="field">PHONE</div></div>
      <div class="form-row"><div class="field area">MESSAGE</div></div>
      <div class="send">SEND NOW</div>
    </div>
    <div class="contact-photo" role="img" aria-label="Round grill loaded with skewers, sausages and vegetables, seen from above"></div>
  </section>

  <footer class="site-footer">
    <div class="footer-col" style="left:70px">
      <h4>QUICK LINKS</h4>
      <ul><li>Home</li><li>About</li><li>Products</li><li>Support Us</li><li>Contact</li></ul>
    </div>
    <div class="footer-col" style="left:250px;width:360px">
      <h4>CONTACT US</h4>
      <div class="contact-line"><span class="icon"><svg width="14" height="14" viewBox="0 0 14 14"><path d="M7 1a4 4 0 0 0-4 4c0 3 4 8 4 8s4-5 4-8a4 4 0 0 0-4-4zm0 5.5A1.5 1.5 0 1 1 7 3.5a1.5 1.5 0 0 1 0 3z" fill="#fff"/></svg></span>48 Ember Lane, Halden,<br>Westport, 7811</div>
      <div class="contact-line"><span class="icon"><svg width="14" height="14" viewBox="0 0 14 14"><path d="M3 1h2l1 3-1.5 1a7 7 0 0 0 4.5 4.5L10 8l3 1v2a2 2 0 0 1-2 2A10 10 0 0 1 1 3a2 2 0 0 1 2-2z" fill="#fff"/></svg></span>+(00) 555 014 2288</div>
      <div class="contact-line"><span class="icon"><svg width="14" height="14" viewBox="0 0 14 14"><rect x="1" y="3" width="12" height="8" rx="1" fill="#fff"/><path d="m1.5 3.5 5.5 4 5.5-4" stroke="#ec4a1c" fill="none"/></svg></span>info@brasato.example</div>
    </div>
    <div class="footer-map" role="img" aria-label="Location map"></div>
    <div class="footer-brand">
      <div class="brand"><span class="brand-dot"></span>BRASATO</div>
      <div class="follow">Follow Us <span class="social"></span><span class="social"></span><span class="social"></span></div>
    </div>
    <div class="copyright">© Copyright - 2021 | Brasato | All Rights Reserved</div>
  </footer>

</div>
</body>
</html>
```